Booklet for meditation CD to match existing CD cover

We need a design for a booklet that matches the meditation CD cover previously designed. It should look like it belongs to the CD as it will be inserted into the cover slot. I hope you can re-use some of the existing artwork. It should incorporate the logo and the text and probably the list of tracks as well. I have attached the original CD cover file, the logo file, photo file and the specs from the CD production company for the 8 page booklet. The spec also includes a cover spec. You can ignore that part. Please put all the text from the CD cover, as well as the track names and the credits from the CD cover into the booklet and the text describing the meditation in full which I have enclosed as a word file.

Target Market(s)

People interested in meditation and personal growth

Font styles to use
Serif

Colors
0555a3
876aae
a54499
e667a6
ee363c

Requirements
Must have
• must match the existing CD cover, must include logo and photo and text from CD cover
• Design, Fonts and colours should match CD cover.

```html
<!DOCTYPE html>
<html lang="en">
<head>
<meta charset="utf-8">
<title>Meditation Booklet – Pages</title>
<link href="https://fonts.googleapis.com/css2?family=Arimo:ital,wght@1,400;1,700&family=Archivo+Narrow:ital,wght@1,400;1,600&display=swap" rel="stylesheet">
<style>
  :root{
    --page-bg:#ffffff;
    --ink:#141414;
    --panel:rgba(255,255,255,0.42);
    --cloud-pink:#d98fb6;
    --cloud-rose:#c97aa6;
    --cloud-light:#f1dbe8;
    --cloud-lilac:#a79ac6;
    --cloud-blue:#7f7fb2;
    --cloud-deep:#6e6fa6;
  }
  html,body{margin:0;padding:0;}
  body{
    width:1200px;height:1188px;overflow:hidden;position:relative;
    background:var(--page-bg);
    font-family:"Arimo",Arial,sans-serif;color:var(--ink);
  }
  .page{position:absolute;width:550px;height:545px;overflow:hidden;}
  .page--intro{left:41px;top:47px;}
  .page--stage-one{left:614px;top:47px;}
  .page--stage-two{left:317px;top:614px;width:549px;}
  .page__artwork{
    position:absolute;inset:0;
    background:
      radial-gradient(ellipse 60% 30% at 55% 62%, var(--cloud-light) 0%, transparent 70%),
      radial-gradient(ellipse 45% 35% at 30% 30%, rgba(255,255,255,0.55) 0%, transparent 70%),
      radial-gradient(ellipse 50% 40% at 80% 20%, var(--cloud-pink) 0%, transparent 70%),
      radial-gradient(ellipse 55% 30% at 20% 85%, var(--cloud-deep) 0%, transparent 75%),
      linear-gradient(180deg, var(--cloud-lilac) 0%, var(--cloud-rose) 35%, var(--cloud-pink) 50%, var(--cloud-lilac) 72%, var(--cloud-blue) 100%);
  }
  .panel{position:absolute;background:var(--panel);box-sizing:border-box;}
  .page--intro .panel{left:107px;top:33px;width:412px;height:417px;padding:17px 11px 0 12px;}
  .page--stage-one .panel{left:106px;top:33px;width:412px;height:486px;padding:15px 10px 0 12px;}
  .page--stage-two .panel{left:15px;top:41px;width:516px;height:470px;padding:9px 17px 0 20px;}
  p{margin:0;font-style:italic;font-size:15px;line-height:19.2px;}
  .justify{text-align:justify;}
  .intro__para{margin-bottom:9px;}
  .stage-title{margin-bottom:8px;}
  .stage-title strong{font-weight:700;}
  .stage-body{padding-left:12px;}
  .stage-body p{margin-bottom:5px;}
  .stage-note{font-weight:700;margin-top:4px;}
  .list-title{font-weight:700;font-size:15.5px;margin:19px 0 11px;}
  .stage-list{list-style:none;margin:0;padding:0 0 0 11px;
    font-family:"Archivo Narrow","Arial Narrow",sans-serif;font-style:italic;font-size:14.5px;line-height:18.5px;}
  .stage-list li{margin-bottom:5px;padding-left:20px;text-indent:-20px;font-weight:600;}
  .stage-list .num{display:inline-block;width:20px;text-indent:0;}
  .stage-list .aside{font-weight:400;font-size:13.5px;}
  .page--stage-two p{font-size:15px;line-height:19.3px;}
</style>
</head>
<body>

<section class="page page--intro">
  <div class="page__artwork" role="img" aria-label="Soft pink and violet cloud artwork with radiating light rays, matching the CD cover"></div>
  <div class="panel">
    <p class="intro__para justify">For this meditation you’ll need a space where you can move freely and preferably have a mattress or soft space for the second and third stages. You’ll need a pillow for the second stage.</p>
    <p class="intro__para">The meditation is in 7 stages that start with movement and move towards stillness.</p>
    <p class="list-title">The seven stages are:</p>
    <ol class="stage-list">
      <li><span class="num">1</span>Shaking (standing)</li>
      <li><span class="num">2</span>Exploring your wild energy <span class="aside">(on the floor or mattress)</span></li>
      <li><span class="num">3</span>Loving yourself in your aliveness <span class="aside">(on the floor or mattress)</span></li>
      <li><span class="num">4</span>Journeying up through each of the energy centres or chakras in the body <span class="aside">(moving mid-way to standing)</span></li>
      <li><span class="num">5</span>Receiving the energy of the infinite standing in that consciousness</li>
      <li><span class="num">6</span>Guided back into sitting in meditation for 15 minutes</li>
      <li><span class="num">7</span>Celebration and returning to your day</li>
    </ol>
  </div>
</section>

<section class="page page--stage-one">
  <div class="page__artwork" role="img" aria-label="Soft pink and violet cloud artwork with radiating light rays, matching the CD cover"></div>
  <div class="panel">
    <p class="stage-title">First stage: <strong>Shaking</strong></p>
    <div class="stage-body">
      <p class="justify">Stand with your feet about hip distance apart, feet firmly planted on the floor. Let your knees be soft and begin to let your body bounce, generating the shaking from your knees so that everything from your pelvis upwards can move freely. Be aware of your body’s limitations. It’s not necessary to shake strongly, it can be a gentle movement. Don’t shake violently. If anything hurts or you are concerned about your body, either make the movement more gentle or lie on the floor and shake your limbs or don’t do it at all.</p>
      <p>Try to keep your whole upper body relaxed, letting go of any holding so that everything can shake (gently, not violently) even your head. Shake everything that you are thinking and feeling. Bring everything down into your body so that your focus of attention is in your body’s aliveness and not in your head. Let your belly, shoulders and jaw be loose.&nbsp; Let your mouth be a little open and relaxed. Let your breathing be as full and easy.</p>
      <p class="stage-note">For this stage, keep any sounds inside.</p>
    </div>
  </div>
</section>

<section class="page page--stage-two">
  <div class="page__artwork" role="img" aria-label="Soft pink and violet cloud artwork with radiating light rays, matching the CD cover"></div>
  <div class="panel">
    <p class="stage-title">Second stage: <strong>Exploring your wild energy</strong></p>
    <div class="stage-body">
      <p class="justify">It’s easier to get into your wild nature if you let yourself be down on the floor so you can roll around, let go and move easily. During this stage you let your body be as wild, free and uninhibited as you can. Start by holding the pillow so that you can use your hands to squeeze it and claw into it.&nbsp; Your mouth may even be biting into the pillow. Make sure you let your hips move. Be uncensored. Let your body have the freedom to move in ways that would be outside its regular habits and pattern. Keep your eyes closed, opening them only to be sure that you aren’t going to hit anything. If you can, let your wild sounds come as well as your wild movements. If that would cause problems, direct your sounds into the pillow. This wild energy may have many different flavours, sometimes all at the same time. It could be wildly happy or angry or sexual. Allow whatever arises and let your body lead you. Beware of going into a repeated pattern of getting angry by beating up someone from the past. Be willing to discover all your energies, not just what you know. Be curious about what is going on in you today. Never mind about what ws happening last time you did it, let today be new and discover yourself today. Give yourself permission to enjoy your uncensored, wild energy. Breathe fully. Move fully. Use your hands and jaw and pelvis to connect with your wildness.</p>
    </div>
  </div>
</section>

</body>
</html>
```